new customer flyer 8.5 X 11 to get people who use CPAP, Snore or have sleep apnea to call us

We sell CPAP equipment and supplies in Ontario. We are designing a flyer for a an advertising campaign encouraging people to switch from the current CPAP supplier to us. Our company name is Breathwell Depot. We are different from a typical CPAP supply store in many ways. A typical store is open 9-5 monday-friday, and the customer must come to the store to get any service. We offer free delivery of supplies of the customer is using the same supplies, so they can just have their supplies shipped rather than come in to pick them up. We also offer free home visits where we will do all the services that can be done in store, including determine the best machine they need, fit them for a mask, set up their equipment and supplies, offer advice, and much more. We also offer night and weekend appointments. Finally we will buy used equipment from our customers and donate this equipment to those in the community who may not be able to afford new equipment, which has 2 benefits of reducing waste and helping the needy.

If you can come up with any other concepts to make us stand out we are open to this.

Our flyer needs to offer a call to action of providing a Prixa Gift card to new customers plus additional call to actions if you are able to create one based on info herein. The gift card amount is $50.00 if this is relevant. We can limit the number available for the promotion if you feel it would encourage a faster and quicker response rate.

The Info needed in the flyer is:
1) Company Name: Breathwell Depot
2) Phone number: 289-517-3064
3) website: www.breathwelldepot-example.com (Make creative in a way that it is easy for user to determine what it says and stimulate them to remember it.)
4) Address is optional, which is 418 Marlow Street, Fort Erie ON L2A 7K3
5) We cover the entire Niagara region and Region of Hamilton in Ontario Canada
6) A call to action is a MUST. We were thinking of using a $50 Prixa gift card for new customers or something else if you feel it would drive more calls to us or more website visits.
7) The objective is to get the customer to call us so we can make them a new customer. The secondary objective is to get the customer to visit our website, because even if they are hesitant to call us, we hope to get them to visit our website and this will give them the confidence to call us.
8) The call to action must encourage a response to hopefully get a call right away. we don't want the customer putting us on the back burner.
9) The flyer is encouraged to not only get people who have sleep apnea, snoring or are currently on CPAP to call, but to also get people who may not suffer from any of these conditions to want to give the flyer to their friends or family who does.
10) I included a bunch of pictures but they are just random pictures, you can use them, use your own or use drawings or whatever to get the message across. You do not need to use all or any of the pictures I provided.
11) We accept all health insurances

I am pretty open, so have fun with the project and be creative as possible!
Updates

There are many designs submitted but many that do not meet the requirements, and many that are similar. I am hoping to find one that does not look like every other generic design, and work with some of the designers who have submitted entries with some potential to modify them into something useable.

Target Market(s)

1) People who snore, have sleep apnea or already use CPAP.
2) Spouses of people snore or have sleep apnea, as these people notice the person who is snoring or having erratic breathing.
3) Friends or family of the people above so that they share the flyer.
4) Focus on 30-60 year old males.

Industry/Entity Type

Advertising

Colors

Designer to choose colors to be used in the design.

Requirements
Must have
• 1) Company Name: Breathwell Depot (Logo can serve as company name as well, files attached)
• 2) Phone number: 289-517-3064
• 3) website: www.breathwelldepot-example.com (Make creative in a way that it is easy for user to determine what it says and stimulate them to remember it.)
• 4) Flyer needs to be friendly and engaging.
• 5) Flyer can be funny or humorous if it will generate customers.
• 6) A call to action is a MUST. We were thinking of using a $50 Prixa gift card for new customers or something else if you feel it would drive more calls to us or more website visits.
• 7) The objective is to get the customer to call us so we can make them a new customer. The secondary objective is to get the customer to visit our website, because even if they are hesitant to call us, we hope to get them to visit our website and this will give them the confidence to call us.
• 8) The call to action must encourage a response to hopefully get a call right away. we don't want the customer putting us on the back burner.
• 9) The flyer is encouraged to not only get people who have sleep apnea, snoring or are currently on CPAP to call, but to also get people who may not suffer from any of these conditions to want to give the flyer to their friends or family who does.
• 10) I included a bunch of pictures but they are just random pictures, you can use them, use your own or use drawings or whatever to get the message across. You do not need to use all or any of the pictures I provided.
• 11) We accept all health insurances
• 12) The FLYER MUST be bold and stand out. This can be with full color, unique text or graphics, or colored backgrounds (Including really bold colors). The point is there is really not a defined market to target with this industry, so any flyers are random location flyers that must be so bold as to grab someones attention such that they want to see what the flyer says.
• 13) Because CPAP only affects about 10-15% of the population, the flyer should be designed that those who snore, suffer from sleep apnea, or CURRENTLY USE CPAP will immediately relate to the flyer and as such want to read it and hopefully call us.
Nice to have
• 1) Address is optional, which is 418 Marlow Street, Fort Erie ON L2A 7K3 (We encourage people to let us come to them, because we offer free shipping and home visits. Therefore our address is not really terribly important.
• 2) We cover the entire Niagara region and Region of Hamilton in Ontario Canada. If they get our flyer they hopefully will call us, however if this can be fit in it confirms that we service the customers area. Without it the customer may wonder if we go to the area where they live.
• 3) Our Taglines are "We make CPAP Personal" and "Better sleep for better health", if they fit into the theme of the designed flyer feel free to add one or both of these.
• 4) The flyer can be designed to appear medical in design if this works, but I prefer fun, engaging and even humorous first, and the medical part becomes secondayry.
Should not have
• 1) The flyer can not be scary or make someone feel uncomfortable.

```html
<!DOCTYPE html>
<html lang="en">
<head>
<meta charset="utf-8">
<title>Breathwell Depot – New Customer Flyer</title>
<link rel="stylesheet" href="https://fonts.googleapis.com/css2?family=Montserrat:wght@400;500;600;700;800;900&family=Raleway:wght@400;500;600&display=swap">
<style>
  :root{
    --purple:#6e388b;
    --purple-light:#8a4fa6;
    --purple-deep:#5c2c78;
    --green:#3fe3a2;
    --gold:#ab9468;
    --ink:#2b2b2b;
    --paper:#f6f5f7;
    --white:#ffffff;
  }
  *{margin:0;padding:0;box-sizing:border-box}
  html,body{width:1000px;height:1200px;overflow:hidden;background:var(--paper)}
  .flyer{position:relative;width:1000px;height:1200px;overflow:hidden;background:var(--paper);font-family:"Raleway",sans-serif;color:var(--ink)}
  .shapes{position:absolute;inset:0}
  .abs{position:absolute}
  .brand{left:44px;top:100px;font-family:"Raleway",sans-serif;font-weight:500;font-size:50px;color:var(--white);letter-spacing:-0.5px;display:flex;align-items:center;gap:12px}
  .brand-dot{width:18px;height:18px;border-radius:50%;background:var(--white)}
  .tagline{left:44px;top:182px;color:var(--white);font-family:"Raleway",sans-serif;line-height:1}
  .tagline .soft{font-size:31px;font-weight:500;display:block}
  .tagline .loud{font-family:"Montserrat",sans-serif;font-weight:900;font-size:37px;color:var(--green);display:block;margin:6px 0 10px}
  .offer{left:66px;top:372px;width:294px;height:196px;text-align:center}
  .offer .get{position:absolute;left:32px;top:72px;transform:rotate(-90deg);transform-origin:left top;font-family:"Montserrat",sans-serif;font-weight:600;font-size:19px;color:var(--purple);letter-spacing:1px}
  .offer .amount{position:absolute;left:62px;top:14px;font-family:"Montserrat",sans-serif;font-weight:900;font-size:72px;color:var(--gold);line-height:1}
  .offer .card{position:absolute;left:0;right:0;top:96px;font-family:"Montserrat",sans-serif;font-weight:800;font-size:20px;color:var(--purple)}
  .offer .note{position:absolute;left:0;right:0;top:120px;font-size:16px;line-height:1.15;font-weight:500}
  .features{left:41px;top:604px;border-left:3px solid var(--purple);padding-left:18px;font-family:"Montserrat",sans-serif;line-height:1}
  .features span{display:block}
  .f-service{font-weight:800;font-size:25px;color:var(--purple);margin-bottom:4px}
  .f-delivery{font-weight:900;font-size:44px;color:var(--gold)}
  .f-local{font-weight:400;font-size:44px;color:var(--purple);margin:2px 0}
  .f-cpap{font-weight:900;font-size:36px;color:var(--gold)}
  .section-title{left:0;right:0;top:770px;text-align:center;font-size:31px;color:var(--purple);font-weight:500;display:flex;justify-content:center;align-items:center;gap:10px}
  .section-title b{font-family:"Montserrat",sans-serif;font-weight:800;color:var(--gold)}
  .section-title i{display:block;width:42px;height:7px;border-top:1px solid var(--gold);border-bottom:1px solid var(--gold);position:relative}
  .perks{left:30px;top:830px;width:940px;display:flex}
  .perk{flex:1;text-align:center;padding:0 12px;border-right:1px solid #c9b7d4}
  .perk:last-child{border-right:none}
  .perk-icon{width:48px;height:48px;margin:0 auto 10px;border-radius:50%;background:var(--purple);display:flex;align-items:center;justify-content:center}
  .perk h3{font-family:"Montserrat",sans-serif;font-weight:700;font-size:19px;color:var(--gold);margin-bottom:6px}
  .perk p{font-size:15.5px;line-height:1.32;color:var(--ink)}
  .coverage{left:40px;top:1053px;width:300px;text-align:center;line-height:1}
  .coverage .small{font-size:17px;color:var(--purple);font-weight:500}
  .coverage .big{font-family:"Montserrat",sans-serif;font-weight:800;font-size:25px;color:var(--gold);display:block;margin:3px 0}
  .contact{right:42px;top:1050px;text-align:right;color:var(--white)}
  .contact .call{font-size:20px;color:var(--gold);font-weight:500}
  .contact .phone{font-family:"Montserrat",sans-serif;font-weight:800;font-size:42px;display:flex;align-items:center;justify-content:flex-end;gap:8px;line-height:1.1}
  .contact .line{font-size:19px;display:flex;align-items:center;justify-content:flex-end;gap:8px;margin-top:4px}
</style>
</head>
<body>
<main class="flyer">
  <svg class="shapes" width="1000" height="1200" viewBox="0 0 1000 1200">
    <defs>
      <linearGradient id="bedroomTone" x1="0" y1="0" x2="1" y2="1">
        <stop offset="0" stop-color="#eef0f4"/>
        <stop offset="0.5" stop-color="#c9ccd6"/>
        <stop offset="1" stop-color="#e6e7ec"/>
      </linearGradient>
      <linearGradient id="outdoorTone" x1="0" y1="0" x2="0" y2="1">
        <stop offset="0" stop-color="#b7b3a6"/>
        <stop offset="0.6" stop-color="#d8b79a"/>
        <stop offset="1" stop-color="#2f3a5c"/>
      </linearGradient>
    </defs>
    <path d="M0,0 H1000 V340 C760,300 560,300 440,360 C300,425 140,450 0,470 Z" fill="var(--purple)"/>
    <path d="M0,0 H1000 V120 C800,40 600,90 420,0 Z" fill="var(--purple-light)" opacity="0.35"/>
    <path d="M990,18 L990,330 C990,505 865,640 700,640 C540,640 430,515 430,360 C430,175 580,55 770,36 Z" fill="var(--white)" stroke="var(--purple)" stroke-width="3"/>
    <path d="M978,30 L978,330 C978,495 858,626 700,626 C548,626 444,508 444,360 C444,185 588,68 770,50 Z" fill="url(#bedroomTone)" role="img" aria-label="Photo of a couple resting in bed, the man wearing a CPAP nasal mask while reading a tablet"/>
    <path d="M66,440 C66,395 100,372 150,372 L290,372 C340,372 360,400 360,440 L360,480 C360,540 300,575 240,572 L150,570 C100,565 66,540 66,500 Z" fill="var(--white)" stroke="var(--purple-light)" stroke-width="3"/>
    <circle cx="822" cy="640" r="128" fill="var(--purple)"/>
    <circle cx="822" cy="640" r="121" fill="var(--white)"/>
    <circle cx="822" cy="640" r="114" fill="url(#outdoorTone)" role="img" aria-label="Photo of a woman outdoors breathing deeply with eyes closed"/>
    <path d="M0,1030 C300,1000 620,1060 1000,1010 V1200 H0 Z" fill="var(--purple)"/>
    <path d="M700,1004 C820,990 920,992 1000,1000" stroke="var(--gold)" stroke-width="3" fill="none"/>
    <path d="M0,1000 C40,1010 70,1030 90,1050" stroke="var(--gold)" stroke-width="6" fill="none"/>
    <path d="M14,1200 V1090 C14,1050 60,1035 120,1035 L260,1035 C330,1050 370,1090 410,1125 C350,1155 310,1200 260,1200 Z" fill="var(--white)" stroke="#d9cde2" stroke-width="3"/>
  </svg>

  <div class="abs brand"><span class="brand-dot"></span>Breathwell Depot</div>

  <div class="abs tagline">
    <span class="soft">We make</span>
    <span class="loud">CPAP PERSONAL</span>
    <span class="soft">Better Sleep for</span>
    <span class="loud">BETTER HEALTH</span>
  </div>

  <div class="abs offer">
    <span class="get">GET A</span>
    <span class="amount">$50</span>
    <span class="card">PRIXA GIFT CARD</span>
    <span class="note">for becoming a<br>new customer</span>
  </div>

  <div class="abs features">
    <span class="f-service">EXPERT CUSTOMER SERVICE</span>
    <span class="f-delivery">FREE DELIVERY</span>
    <span class="f-local">LOCALLY OWNED</span>
    <span class="f-cpap">ALL WE DO IS CPAP</span>
  </div>

  <h2 class="abs section-title"><i></i>Taking care of <b>YOUR HEALTH</b><i></i></h2>

  <section class="abs perks">
    <article class="perk">
      <div class="perk-icon"><svg width="26" height="22" viewBox="0 0 26 22"><ellipse cx="10" cy="9" rx="9" ry="7" fill="#fff"/><ellipse cx="17" cy="12" rx="8" ry="6" fill="#fff" opacity="0.85"/><path d="M5,14 L3,20 L10,15 Z" fill="#fff"/></svg></div>
      <h3>We Love to Talk</h3>
      <p>Breathwell Depot loves to chat. We will talk to anyone about CPAP (You don't even need to be a customer! ...</p>
    </article>
    <article class="perk">
      <div class="perk-icon"><svg width="22" height="22" viewBox="0 0 22 22"><circle cx="11" cy="7" r="5" fill="#fff"/><path d="M2,21 C2,14 20,14 20,21 Z" fill="#fff"/></svg></div>
      <h3>We Only do CPAP</h3>
      <p>CPAP is our passion, and we are experts in it. When you love CPAP as much as we do, there is nothing else...</p>
    </article>
    <article class="perk">
      <div class="perk-icon"><svg width="28" height="20" viewBox="0 0 28 20"><rect x="1" y="3" width="16" height="11" fill="#fff"/><path d="M18,7 H23 L27,11 V14 H18 Z" fill="#fff"/><circle cx="6" cy="16" r="3" fill="#fff" stroke="var(--purple)" stroke-width="1.5"/><circle cx="22" cy="16" r="3" fill="#fff" stroke="var(--purple)" stroke-width="1.5"/></svg></div>
      <h3>FREE Delivery</h3>
      <p>You may not drive or be too busy at work, but no matter the reason, we offer FREE delivery to all ...</p>
    </article>
  </section>

  <div class="abs coverage">
    <span class="small">We cover the entire</span>
    <span class="big">NIAGARA REGION<br>AND REGION OF<br>HAMILTON</span>
    <span class="small">in Ontario Canada</span>
  </div>

  <div class="abs contact">
    <div class="call">Call Us At (Anytime!)</div>
    <div class="phone"><svg width="18" height="30" viewBox="0 0 18 30"><path d="M14,2 C6,4 3,10 3,15 C3,20 6,26 14,28" stroke="#fff" stroke-width="3" fill="none" stroke-linecap="round"/></svg>289-517-3064</div>
    <div class="line"><svg width="14" height="18" viewBox="0 0 14 18"><path d="M7,17 C3,11 1,8 1,6 A6,6 0 0 1 13,6 C13,8 11,11 7,17 Z" stroke="#fff" stroke-width="1.5" fill="none"/><circle cx="7" cy="6" r="2" fill="#fff"/></svg>418 Marlow Street, Fort Erie ON L2A 7K3</div>
    <div class="line"><svg width="16" height="16" viewBox="0 0 16 16"><circle cx="8" cy="8" r="7" stroke="#fff" stroke-width="1.3" fill="none"/><ellipse cx="8" cy="8" rx="3" ry="7" stroke="#fff" stroke-width="1.2" fill="none"/><path d="M1,8 H15" stroke="#fff" stroke-width="1.2"/></svg>www.breathwelldepot-example.com</div>
  </div>
</main>
</body>
</html>
```